Digital content business needs banner ads

We sell content - if you need an article to put on your website or in a newsletter, you can purchase a ready made article from us and edit it to your liking to use straight away. This could be any kind of article, but this banner ad will be aimed at real estate agents. You can see the website (and the style of articles) here https://www.thecopperwrenpost.com.au
The banner is meant to solve the problem of the front desk admin or agent trying to think of something to write to put in their email newsletter. This will save them time as they can just select an article from our library and use it (for a fee of course!).
Needs to have the words:
--------------------------------------------------
Find the next article for your newsletter
---------------------------------------------------
Some imagery would be good rather than plain text.
With a call to action like click here button or similar
Required sizes (or provide a set of standard sized ads):
728 x 90
970 x 250
300x250
Target Market(s)
Real Estate Agents

```html
<!DOCTYPE html>
<html lang="en">
<head>
<meta charset="utf-8">
<title>The Copper Wren Post – Find the next article for your newsletter</title>
<link href="https://fonts.googleapis.com/css2?family=Open+Sans:wght@400;700;800&display=swap" rel="stylesheet">
<style>
  :root {
    --panel-dark: #3d3e40;
    --accent-blue: #1b86cf;
    --button-blue: #1f7fcc;
    --text-light: #ffffff;
    --brand-blue: #1f6fb8;
    --photo-warm-1: #f4f2ee;
    --photo-warm-2: #d9c7ad;
    --photo-warm-3: #b9936a;
    --photo-cool-1: #f3f4f5;
    --photo-cool-2: #c9ced3;
    --photo-cool-3: #8c949c;
  }
  * { margin: 0; padding: 0; box-sizing: border-box; }
  html, body {
    width: 1200px; height: 148px; overflow: hidden; background: #ffffff;
  }
  .banner {
    position: relative; width: 1200px; height: 148px; overflow: hidden;
    font-family: "Open Sans", Arial, sans-serif;
  }
  .hero-photo {
    position: absolute; top: 0; left: 0; width: 520px; height: 148px;
    background: linear-gradient(100deg, var(--photo-warm-1) 0%, var(--photo-warm-1) 25%, var(--photo-warm-2) 55%, var(--photo-warm-3) 80%, var(--photo-warm-2) 100%);
  }
  .house-photo {
    position: absolute; top: 0; right: 0; width: 280px; height: 148px;
    background: linear-gradient(110deg, var(--photo-cool-2) 0%, var(--photo-cool-1) 45%, var(--photo-cool-3) 100%);
  }
  .panel-shape { position: absolute; inset: 0; }
  .brand {
    position: absolute; left: 14px; top: 10px; width: 136px; height: 126px;
    background: #ffffff; border-radius: 14px;
    display: flex; align-items: center; gap: 8px; padding: 0 12px;
    box-shadow: 0 2px 6px rgba(0,0,0,0.12);
  }
  .brand-mark { width: 12px; height: 12px; background: var(--brand-blue); flex: none; }
  .brand-name {
    color: var(--brand-blue); font-weight: 800; font-size: 17px; line-height: 1.1;
    text-transform: uppercase;
  }
  .headline {
    position: absolute; left: 500px; width: 452px; top: 36px;
    color: var(--text-light); text-align: center;
    font-size: 32px; line-height: 42px; font-weight: 400;
  }
  .headline strong { font-weight: 700; }
  .cta {
    position: absolute; left: 997px; top: 44px; width: 176px; height: 62px;
    background: var(--button-blue); color: var(--text-light);
    display: flex; align-items: center; justify-content: center;
    font-size: 26px; font-weight: 400; text-decoration: none;
  }
</style>
</head>
<body>
  <div class="banner">
    <div class="hero-photo" role="img" aria-label="Magnifying glass over small wooden house models on a desk"></div>
    <div class="house-photo" role="img" aria-label="Small white model house on a table"></div>

    <svg class="panel-shape" width="1200" height="148" viewBox="0 0 1200 148" aria-hidden="true">
      <polygon points="497,0 972,0 950,148 475,148" fill="var(--panel-dark)"/>
      <polygon points="489,0 499,0 477,148 467,148" fill="var(--accent-blue)"/>
      <polygon points="970,0 980,0 958,148 948,148" fill="var(--accent-blue)"/>
    </svg>

    <div class="brand">
      <span class="brand-mark"></span>
      <span class="brand-name">The Copper Wren Post</span>
    </div>

    <h1 class="headline">
      <strong>Find</strong> the <strong>next article</strong><br>
      for <strong>your newsletter</strong>
    </h1>

    <a class="cta" href="https://www.thecopperwrenpost.com.au">Click Here</a>
  </div>
</body>
</html>
```